Process Roadmap for Interior Design Firm

We are looking to ramp up the design appeal of our current process roadmap to be very visually interesting, while staying informative and descriptive about our process.

Target Market(s)

In-house Clients

Industry/Entity Type

Interior Design Firm focused on sustainable and holistic design.

Other font styles liked:
• raleway

Requirements
Must have
• 1.) it would be nice if the graphic provided a more clear indication of the “journey” from one step to the next, so that there was a clear sense of the progression (such that we are directing the viewer) 2.). We would want it to fit on an 8.5”x11” page (the page could be horizontal when we have the Calm Compass formatted out with the testimonials) (in addition to the testimonials, we may also want to have the detailed descriptions of each step of the process presented below the graphic, so that the graphic is cleaner) 3.) ideally the graphic is clear and simple enough to also be used on our Bi-Weekly Client Updates, which will be typed updates for clients re their project budgets, schedule and scope. The Calm Compass graphic (without all the testimonials) would be at the end of the update, and would fit on the page horizontally at the bottom, perhaps in a space which is 7.5”w x 4”h or so.
Should not have
• bold or bright colors. Natural neutrals are preferred, such as the ones featured on the provided graphic.

```html
<!DOCTYPE html>
<html lang="en">
<head>
<meta charset="utf-8">
<title>Our Calm Compass</title>
<link href="https://fonts.googleapis.com/css2?family=Raleway:wght@400;500;700;800&display=swap" rel="stylesheet">
<style>
  :root {
    --page: #f2f2f2;
    --sheet: #fdfcfa;
    --band: #f0e9d8;
    --ink: #2e2a28;
    --ink-soft: #3a3432;
    --gold: #b8924f;
    --tan: #c9baa0;
    --path: #e4e4e4;
    --ring-dark: #3b2b26;
  }
  * { margin: 0; padding: 0; box-sizing: border-box; }
  html, body { width: 1200px; height: 884px; overflow: hidden; }
  body {
    background: var(--page);
    font-family: "Raleway", sans-serif;
    color: var(--ink);
    position: relative;
  }
  .sheet {
    position: absolute; left: 141px; top: 52px; width: 917px; height: 710px;
    background: var(--sheet);
  }
  .testimonial-band {
    position: absolute; left: 141px; top: 565px; width: 917px; height: 197px;
    background: var(--band);
  }
  .roadmap-art { position: absolute; left: 0; top: 0; width: 1200px; height: 884px; }
  .firm-name {
    position: absolute; left: 420px; top: 106px; width: 360px;
    text-align: center; color: var(--gold);
    font-size: 17px; font-weight: 500; letter-spacing: 0.04em; line-height: 1;
  }
  .headline {
    position: absolute; left: 300px; top: 176px; width: 606px;
    text-align: center; font-size: 42px; font-weight: 700; color: var(--ink);
  }
  .headline em { font-style: normal; color: var(--gold); }
  .step {
    position: absolute; text-align: center; transform: translateX(-50%);
  }
  .step-title {
    font-size: 14px; font-weight: 800; letter-spacing: 0.01em; color: var(--ink);
    margin-bottom: 10px;
  }
  .step-text {
    font-size: 9.3px; line-height: 1.25; color: var(--ink-soft);
  }
  .step-text + .step-text { margin-top: 10px; }
  .testimonials-title {
    position: absolute; left: 400px; top: 591px; width: 400px;
    text-align: center; font-size: 25px; font-weight: 700; color: var(--ink);
  }
  .testimonial {
    position: absolute; top: 643px; width: 178px;
    font-size: 8.7px; line-height: 1.27; color: var(--ink-soft);
  }
</style>
</head>
<body>
  <div class="sheet"></div>
  <div class="testimonial-band"></div>

  <svg class="roadmap-art" viewBox="0 0 1035 763" aria-hidden="true">
    <defs>
      <g id="step-ring">
        <circle r="37" fill="none" stroke="var(--ring-dark)" stroke-width="1" stroke-dasharray="1 2.2"/>
        <path d="M-37 0 A37 37 0 0 1 37 0" fill="none" stroke="var(--ring-dark)" stroke-width="1.2"/>
        <circle r="31" fill="#ffffff"/>
        <circle r="27" fill="#ffffff" stroke="var(--tan)" stroke-width="7"/>
        <circle cy="-37" r="4.2" fill="#f0e2c4" stroke="var(--gold)" stroke-width="1.2"/>
        <circle cy="-37" r="1.6" fill="var(--gold)"/>
      </g>
    </defs>

    <path d="M228 192 C 250 250, 320 272, 414 282 C 480 290, 560 292, 630 282 C 700 272, 760 245, 790 205 C 815 170, 812 125, 778 97"
          fill="none" stroke="var(--path)" stroke-width="7" stroke-linecap="round"/>
    <polygon points="756,78 786,86 770,104" fill="var(--path)"/>

    <g fill="none" stroke="var(--ink)" stroke-width="1.4" stroke-linecap="round" stroke-linejoin="round">
      <g transform="translate(231 155)">
        <use href="#step-ring"/>
        <circle cy="-1" r="3.5"/>
        <path d="M-6 4 A7.5 7.5 0 1 1 6 4"/>
        <path d="M-9 8 A12 12 0 1 1 9 8"/>
        <path d="M-3 11 L0 3 L3 11"/>
      </g>
      <g transform="translate(309 243)">
        <use href="#step-ring"/>
        <path d="M-12 0 Q0 -10 12 0 Q0 10 -12 0Z"/>
        <circle r="4"/>
        <circle r="1.4" fill="var(--ink)"/>
      </g>
      <g transform="translate(414 279)">
        <use href="#step-ring"/>
        <rect x="-10" y="-8" width="15" height="18" rx="1"/>
        <path d="M-7 -3 H1 M-7 1 H1 M-7 5 H-1"/>
        <path d="M2 4 L11 -7 L13 -5 L4 6 L1 7Z"/>
      </g>
      <g transform="translate(517 286)">
        <use href="#step-ring"/>
        <rect x="-11" y="-10" width="20" height="18" rx="1"/>
        <path d="M-7 5 L5 -7 L5 5Z"/>
        <path d="M3 7 L12 -4"/>
      </g>
      <g transform="translate(620 279)">
        <use href="#step-ring"/>
        <circle r="10" stroke-width="3" stroke-dasharray="2.6 2.6"/>
        <circle r="7"/>
        <path d="M0 -4 V0 L3 2"/>
      </g>
      <g transform="translate(723 243)">
        <use href="#step-ring"/>
        <circle cx="-2" cy="-3" r="6" stroke-width="2.6" stroke-dasharray="2.2 2.2"/>
        <circle cx="-2" cy="-3" r="2.5"/>
        <path d="M-12 7 H12"/>
        <circle cx="-8" cy="7" r="2.5"/>
        <circle cx="8" cy="7" r="2.5"/>
      </g>
      <g transform="translate(806 155)">
        <use href="#step-ring"/>
        <path d="M0 1 C-7 -4 -5 -10 0 -6 C5 -10 7 -4 0 1Z"/>
        <path d="M-13 -2 V6 L-6 12 H-2 V7 L-7 3"/>
        <path d="M13 -2 V6 L6 12 H2 V7 L7 3"/>
        <path d="M0 -14 V-11 M-6 -12 L-5 -10 M6 -12 L5 -10"/>
      </g>
    </g>
  </svg>

  <p class="firm-name">Ross Halloran Design</p>

  <h1 class="headline">Our <em>Calm Compass</em></h1>

  <div class="step" style="left:265px; top:238px; width:96px;">
    <h2 class="step-title">LISTENING</h2>
    <p class="step-text">Listening to our clients, their land, and their home.</p>
    <p class="step-text">Identifying their needs, challenges, wishes, and dreams.</p>
  </div>

  <div class="step" style="left:358px; top:340px; width:106px;">
    <h2 class="step-title">VISIONING</h2>
    <p class="step-text">Facilitating a guided visioning process to clarify the deepest intention, true purpose, and highest potential for their home and their future within it.</p>
  </div>

  <div class="step" style="left:480px; top:380px; width:100px;">
    <h2 class="step-title">PLANNING</h2>
    <p class="step-text">Turning our client's vision into a clearly defined scope, budget, and timeline.</p>
    <p class="step-text">Mapping out the steps for making their dream a reality.</p>
    <p class="step-text">Setting a meeting schedule from start to finish.</p>
  </div>

  <div class="step" style="left:599px; top:406px; width:118px;">
    <h2 class="step-title">DESIGNING</h2>
    <p class="step-text">Following the schedule through the design phases from initial design concepts, technical drawings and details, and the selection of all finishes, fixtures, and furnishings.</p>
  </div>

  <div class="step" style="left:719px; top:380px; width:108px;">
    <h2 class="step-title">MANAGING</h2>
    <p class="step-text">Coordinating with clients, builders, architects, and vendors to ensure that the design is executed with excellence, and the construction and furnishings are on-time and on-budget.</p>
  </div>

  <div class="step" style="left:840px; top:340px; width:108px;">
    <h2 class="step-title">INSTALLING</h2>
    <p class="step-text">Overseeing the inspection, installation, and arrangement of all furnishings, lighting, artwork, and decorative items.</p>
    <p class="step-text">Taking care of every last detail.</p>
  </div>

  <div class="step" style="left:940px; top:238px; width:100px;">
    <h2 class="step-title">COMPLETING</h2>
    <p class="step-text">Fixing any issues or defects.</p>
    <p class="step-text">Follow up on all remaining items.</p>
    <p class="step-text">Completing the final finishing touches to our client's full and total satisfaction.</p>
  </div>

  <h2 class="testimonials-title">Testimonials</h2>
  <p class="testimonial" style="left:192px;">Lorem ipsum dolor sit amet, consectetuer adipiscing elit, sed diam nonummy nibh euismod tincidunt ut laoreet dolore magna aliquam erat volutpat. Ut wisi enim ad minim veniam, quis nostrud exerci tation ullamcorper suscipit lobortis nisl ut</p>
  <p class="testimonial" style="left:407px;">Lorem ipsum dolor sit amet, consectetuer adipiscing elit, sed diam nonummy nibh euismod tincidunt ut laoreet dolore magna aliquam erat volutpat. Ut wisi enim ad minim veniam, quis nostrud exerci tation ullamcorper suscipit lobortis nisl ut</p>
  <p class="testimonial" style="left:620px;">Lorem ipsum dolor sit amet, consectetuer adipiscing elit, sed diam nonummy nibh euismod tincidunt ut laoreet dolore magna aliquam erat volutpat. Ut wisi enim ad minim veniam, quis nostrud exerci tation ullamcorper suscipit lobortis nisl ut</p>
  <p class="testimonial" style="left:833px;">Lorem ipsum dolor sit amet, consectetuer adipiscing elit, sed diam nonummy nibh euismod tincidunt ut laoreet dolore magna aliquam erat volutpat. Ut wisi enim ad minim veniam, quis nostrud exerci tation ullamcorper suscipit lobortis nisl ut</p>
</body>
</html>
```